Banner Design 4040mm W x 2190mm H

Design a glamorous and exciting 4040mm W x 2190mm H backdrop for the QRLMT Velvet Orchid Gala at the luxurious Tallow Hall, Fenwick, Mirrabelle, Sydney. This exciting backdrop should be spectacular so that people will be excited to take photos in front of it.
Design Colours preferred is black and pink.
Please include our website on the banner www.qrlmt.org.au
Should include the words "QRLMT Velvet Orchid Gala" as the main attraction on the banner.
Please include "Thank you to our sponsors" and include the logo of the sponsors.
Sponsors:
Brockden Pathology
EastGlen Radiology
KTV Diagnostic Imaging
Harbin Legal Group
Truffords
Banner Template:
4040mm W x 2190mm H Single Sided (.AI)
https://files.example-share.net/d/8ZkQm3TnWp47LcVbXr2YhJd5Fs61Ae/view
QRLMT Logo:
Can be obtained from our website www.qrlmt.org.au

```html
<!DOCTYPE html>
<html lang="en">
<head>
<meta charset="utf-8">
<title>QRLMT Velvet Orchid Gala – Backdrop</title>
<link rel="stylesheet" href="https://fonts.googleapis.com/css2?family=Barlow:wght@400;500;700&family=Great+Vibes&family=Playfair+Display:ital@1&display=swap">
<style>
  :root {
    --page-bg: #bdbdbd;
    --banner-black: #070707;
    --orchid-pink: #c94a98;
    --white: #ffffff;
    --sponsor-frame: #111111;
    --ink-red: #d3184f;
    --ink-navy: #1d3a7a;
    --ink-purple: #6a4a9c;
    --ink-gold: #c99a1e;
    --ink-blue: #17386b;
  }
  html, body {
    margin: 0;
    width: 1200px;
    height: 1200px;
    overflow: hidden;
    background: var(--page-bg);
  }
  .canvas {
    position: relative;
    width: 1200px;
    height: 1200px;
  }
  .backdrop {
    position: absolute;
    left: 40px;
    top: 296px;
    width: 1120px;
    height: 607px;
    display: block;
  }
  .banner-field { fill: var(--banner-black); }
  .hero-arc { fill: var(--orchid-pink); }
  .org-mark { fill: none; stroke: var(--white); stroke-width: 3; }
  .org-name {
    font-family: "Barlow", Arial, sans-serif;
    font-weight: 500;
    font-size: 42px;
    fill: var(--white);
  }
  .event-title {
    font-family: "Great Vibes", cursive;
    font-size: 74px;
    fill: var(--white);
  }
  .event-tagline {
    font-family: "Barlow", Arial, sans-serif;
    font-weight: 400;
    font-size: 16px;
    letter-spacing: 1px;
    fill: var(--white);
  }
  .website {
    font-family: "Barlow", Arial, sans-serif;
    font-weight: 700;
    font-size: 40px;
    letter-spacing: 5px;
    fill: var(--white);
  }
  .sponsor-thanks {
    font-family: "Playfair Display", Georgia, serif;
    font-style: italic;
    font-size: 34px;
    fill: var(--orchid-pink);
  }
  .sponsor-card { fill: var(--white); }
  .sponsor-card-line { fill: none; stroke: var(--sponsor-frame); stroke-width: 1.5; }
  .sponsor-name {
    font-family: "Barlow", Arial, sans-serif;
    font-weight: 700;
    font-size: 17px;
  }
  .sponsor-brockden { fill: var(--ink-red); }
  .sponsor-eastglen { fill: var(--ink-navy); }
  .sponsor-ktv { fill: var(--ink-purple); }
  .sponsor-harbin { fill: var(--ink-gold); }
  .sponsor-truffords { fill: var(--ink-blue); }
</style>
</head>
<body>
<main class="canvas">
  <svg class="backdrop" viewBox="0 0 1375 745" xmlns="http://www.w3.org/2000/svg" aria-label="QRLMT Velvet Orchid Gala backdrop">
    <defs>
      <clipPath id="banner-shape">
        <path d="M0 40 Q0 0 40 0 H1335 Q1375 0 1375 40 V745 H0 Z"/>
      </clipPath>
      <path id="website-curve" d="M273 5 A415 415 0 0 0 1103 5"/>
    </defs>

    <g clip-path="url(#banner-shape)">
      <rect class="banner-field" x="0" y="0" width="1375" height="745"/>
      <circle class="hero-arc" cx="688" cy="0" r="373"/>
    </g>

    <g class="event-heading" text-anchor="middle">
      <circle class="org-mark" cx="688" cy="100" r="48"/>
      <text class="org-name" x="688" y="206">QRLMT</text>
      <text class="event-title" x="688" y="284">Velvet Orchid Gala</text>
      <text class="event-tagline" x="688" y="318">SOCIAL AND SPORTING EVENTS</text>
    </g>

    <text class="website" text-anchor="middle">
      <textPath href="#website-curve" startOffset="50%">www.qrlmt.org.au</textPath>
    </text>

    <text class="sponsor-thanks" x="688" y="514" text-anchor="middle">“Thank you to our sponsors”</text>

    <g class="sponsor-row" text-anchor="middle" dominant-baseline="middle">
      <g class="sponsor">
        <rect class="sponsor-card" x="153" y="542" width="182" height="58"/>
        <rect class="sponsor-card-line" x="157" y="546" width="174" height="50"/>
        <text class="sponsor-name sponsor-brockden" x="244" y="571">Brockden Pathology</text>
      </g>
      <g class="sponsor">
        <rect class="sponsor-card" x="372" y="542" width="224" height="58"/>
        <rect class="sponsor-card-line" x="376" y="546" width="216" height="50"/>
        <text class="sponsor-name sponsor-eastglen" x="484" y="571">EastGlen Radiology</text>
      </g>
      <g class="sponsor">
        <rect class="sponsor-card" x="632" y="542" width="197" height="58"/>
        <rect class="sponsor-card-line" x="636" y="546" width="189" height="50"/>
        <text class="sponsor-name sponsor-ktv" x="730" y="571">KTV Diagnostic Imaging</text>
      </g>
      <g class="sponsor">
        <rect class="sponsor-card" x="864" y="542" width="174" height="58"/>
        <rect class="sponsor-card-line" x="868" y="546" width="166" height="50"/>
        <text class="sponsor-name sponsor-harbin" x="951" y="571">Harbin Legal Group</text>
      </g>
      <g class="sponsor">
        <rect class="sponsor-card" x="1072" y="542" width="156" height="58"/>
        <rect class="sponsor-card-line" x="1076" y="546" width="148" height="50"/>
        <text class="sponsor-name sponsor-truffords" x="1150" y="571">Truffords</text>
      </g>
    </g>
  </svg>
</main>
</body>
</html>
```